Local Electrical company need some kick ass business cards

In need of some in your face design business cards for a family owned electrical service company in Edmonton, Alberta Canada. We provide reliable and trustworthy electrical service for commercial and residential work in the Edmonton and area. We have been in business for 25 years.

Target Market(s)

Residential and commercial electrical

Industry/Entity Type

Business

Contact Information for Business Card

Your welcome to change and modify the brightway electric logo. please include the lightbulb! Our Colours are black and green please stay with that.
Please include a name phone number and address on the card
phone number - 780-318-5062
#22, 418 Maple Cres, St.Albert, Alberta.
Two things that need to be on the card.
"your friendly neighborhood electrictrician"
Commercial & residential electrical repair and service

Colors
9bcb3c

Requirements
Must have
• Light bulb guy Attached
• "your friendly neighborhood electrictrician"
• Commercial & residential electrical repair and service
• phone number - 780-318-5062
• #22, 418 Maple Cres, St.Albert, Alberta.
• Our colours are black and green
Nice to have
• go wild i want something loud

```html
<!DOCTYPE html>
<html lang="en">
<head>
<meta charset="utf-8">
<title>Brightway Electric – Business Card</title>
<link rel="stylesheet" href="https://fonts.googleapis.com/css2?family=Open+Sans:wght@400;600;700;800&display=swap">
<style>
  :root {
    --green: #9bcb3c;
    --green-deep: #4f9a2a;
    --green-mid: #6db33f;
    --ink: #1c1c1c;
    --charcoal: #2b2b2b;
    --paper: #f4f4f2;
    --stage: #8a8f93;
    --white: #ffffff;
  }
  * { box-sizing: border-box; margin: 0; padding: 0; }
  html, body { width: 1200px; height: 902px; overflow: hidden; }
  body {
    background: var(--stage);
    font-family: "Open Sans", Arial, sans-serif;
    position: relative;
  }
  .card {
    position: absolute;
    top: 136px;
    width: 360px;
    height: 630px;
    overflow: hidden;
    box-shadow: 0 10px 30px rgba(0,0,0,.35);
  }
  /* front */
  .card--front { left: 200px; background: var(--paper); border-left: 12px solid var(--charcoal); }
  .front-logo {
    position: absolute; top: 88px; left: 0; right: 0;
    display: flex; align-items: center; justify-content: center; gap: 10px;
  }
  .front-logo__dot { width: 20px; height: 20px; border-radius: 50%; background: var(--green); flex: none; }
  .front-logo__name {
    font-weight: 800; font-size: 24px; letter-spacing: 1px; color: var(--ink);
    text-transform: uppercase; white-space: nowrap;
  }
  .front-ribbon { position: absolute; left: 0; top: 230px; }
  .front-badge { position: absolute; right: 0; top: 290px; }
  .front-mascot {
    position: absolute; right: 17px; top: 309px; width: 30px; height: 34px; border-radius: 50%;
    background: radial-gradient(circle, #f2f2f2, #b9d98a);
  }
  .front-name {
    position: absolute; top: 236px; left: 150px;
    font-weight: 800; font-size: 21px; line-height: 1.05; color: var(--ink); text-transform: uppercase;
  }
  .front-name__sub { font-size: 15px; letter-spacing: 3px; }
  .contact { position: absolute; left: 132px; font-size: 13.5px; color: var(--ink); white-space: nowrap; }
  .contact--phone { top: 302px; font-size: 16px; letter-spacing: 1px; }
  .contact--web { top: 384px; font-size: 11px; }
  .contact--address { top: 430px; width: 200px; line-height: 1.4; white-space: normal; }
  .front-services {
    position: absolute; left: 0; right: 0; bottom: 22px;
    text-align: center; font-size: 12px; font-weight: 600; color: var(--ink);
  }
  /* back */
  .card--back {
    left: 640px;
    background:
      repeating-linear-gradient(90deg, rgba(255,255,255,.025) 0 1px, transparent 1px 4px),
      radial-gradient(circle at 50% 38%, #4a4a4a 0%, #262626 55%, #141414 100%);
    border-left: 10px solid var(--green-mid);
  }
  .back-band {
    position: absolute; top: 0; right: 0; width: 34px; height: 100%;
    background: linear-gradient(90deg, var(--green-deep), var(--green) 50%, var(--green-deep));
  }
  .back-mascot {
    position: absolute; left: 60px; top: 130px; width: 220px; height: 220px; border-radius: 50%;
    background: radial-gradient(circle, #eef2e6 0%, #c9e88a 30%, rgba(155,203,60,.35) 55%, transparent 72%);
  }
  .back-tagline {
    position: absolute; left: 22px; bottom: 26px;
    font-size: 13px; color: var(--white); letter-spacing: .2px;
  }
</style>
</head>
<body>
  <section class="card card--front" aria-label="Card front">
    <div class="front-logo">
      <span class="front-logo__dot"></span>
      <span class="front-logo__name">Brightway Electric</span>
    </div>

    <svg class="front-ribbon" width="120" height="220" viewBox="0 0 120 220" aria-hidden="true">
      <polygon points="0,0 100,0 120,20 120,200 0,220" fill="var(--green-deep)"/>
      <polygon points="0,10 108,10 108,205 0,212" fill="var(--green)"/>
      <polygon points="80,22 98,32 98,54 80,64 62,54 62,32" fill="var(--green-deep)"/>
      <path d="M74,34 q-3,9 6,18 l4,-3 -4,-4 -2,1 q-3,-3 -3,-7 l2,-1 -1,-5z" fill="var(--white)"/>
      <polygon points="56,70 74,80 74,102 56,112 38,102 38,80" fill="var(--green-deep)"/>
      <g fill="none" stroke="var(--white)" stroke-width="1.6">
        <circle cx="56" cy="91" r="10"/>
        <ellipse cx="56" cy="91" rx="4.5" ry="10"/>
        <line x1="46" y1="91" x2="66" y2="91"/>
      </g>
      <polygon points="32,118 50,128 50,150 32,160 14,150 14,128" fill="var(--green-deep)"/>
      <path d="M22,140 l10,-9 10,9 h-3 v9 h-14 v-9z" fill="var(--white)"/>
    </svg>

    <div class="front-name">Brightway<br><span class="front-name__sub">Electric</span></div>

    <svg class="front-badge" width="70" height="74" viewBox="0 0 70 74" aria-hidden="true">
      <polygon points="14,0 70,0 70,74 14,74 0,60 0,14" fill="var(--green)"/>
      <polygon points="38,12 58,24 58,48 38,60 18,48 18,24" fill="var(--green-deep)"/>
    </svg>
    <div class="front-mascot" role="img" aria-label="Small lightbulb mascot wearing a green cap"></div>

    <p class="contact contact--phone">780-318-5062</p>
    <p class="contact contact--web">http://www.brightwayelectricltd.com</p>
    <p class="contact contact--address">#22, 418 Maple Cres, St.Albert, Alberta.</p>

    <p class="front-services">Commercial &amp; residential electrical repair and service</p>
  </section>

  <section class="card card--back" aria-label="Card back">
    <div class="back-band"></div>
    <div class="back-mascot" role="img" aria-label="Cartoon lightbulb character in a green and white cap with a green electric glow"></div>
    <p class="back-tagline">your friendly neighborhood electrictrician</p>
  </section>
</body>
</html>
```